PowerPoint template design for TLBavendish Consulting

I'm interested in a PowerPoint template design that incorporates my logo (see attached file). I am an economist who mostly shows charts and tables in Calibri 24 point. Most tables are 4 or 5 columns by 14 or 15 rows so the design should seek to maximize work space on the slide while unmistakably indicating that these are my slides. I will be using the template design when I provide copies of my slides to the audience after the presentation, mostly in PDF format.

Target Market(s)

Mostly non-data types including educators.

Industry/Entity Type

Consulting

Font styles to use
Sans Serif

Colors
00a990
33b8a4
86cfc6

Requirements
Must have
• Looking for something more sleek and subtle, that doesn't take up too much screen real estate and that in some manner incorporates my business card/logo design. The logo doesn't have to be exactly incorporated as is, but it should visually align or mesh. I like the teal and gray/dark gray color palette that is on my business card.
Nice to have
• Open to more transparency/faded coloring, less bold and vivid than subtle background.
Should not have
• The goal is a PP template design that is unmistakably mine but is not so intrusive that it is the focus of every slide. I want the viewer to forget that the slide is coming from me as a consultant and focus on the content of the slide. I'm not using this as part of a marketing or advertising push as much as I am marking my material so folks who refer to the slides at a later date will know that they are mine.

```html
<!DOCTYPE html>
<html lang="en">
<head>
<meta charset="utf-8">
<title>TLBavendish Consulting – Slide Template</title>
<link href="https://fonts.googleapis.com/css2?family=Carlito:wght@400;700&display=swap" rel="stylesheet">
<style>
  :root {
    --teal: #00a990;
    --teal-mid: #33b8a4;
    --teal-light: #86cfc6;
    --teal-pale: #e4f4f1;
    --ink: #333a3f;
    --gray-dark: #4d5459;
    --gray: #9aa1a5;
    --gray-light: #e9ecec;
    --row-alt: #f3f5f5;
    --paper: #ffffff;
    --canvas: #ffffff;
  }
  * { box-sizing: border-box; margin: 0; padding: 0; }
  html, body {
    width: 1200px; height: 2644px; overflow: hidden;
    background: var(--canvas);
    font-family: "Carlito", "Calibri", Arial, sans-serif;
    color: var(--ink);
  }
  .deck { position: relative; width: 1200px; height: 2644px; }
  .slide {
    position: absolute; left: 8px; width: 1184px; height: 860px;
    background: var(--paper);
    border: 2px solid var(--gray-light);
    box-shadow: 0 2px 6px rgba(0,0,0,0.12);
    overflow: hidden;
  }
  .slide--one { top: 0; }
  .slide--two { top: 892px; }
  .slide--three { top: 1784px; }

  .slide-header {
    height: 82px; display: flex; align-items: center; justify-content: space-between;
    padding: 0 28px 0 36px;
    border-bottom: 5px solid var(--teal);
  }
  .slide-header--light { background: var(--gray-light); }
  .slide-header--solid { background: var(--teal); border-bottom-color: var(--teal-light); }
  .slide-header--pale { background: var(--teal-pale); border-bottom-color: var(--teal-mid); }

  .slide-title {
    font-size: 30px; font-weight: 700; letter-spacing: 0.5px; color: var(--gray-dark);
  }
  .slide-header--solid .slide-title { color: var(--paper); }

  .brand {
    display: flex; align-items: center; gap: 10px;
    background: var(--paper); padding: 8px 14px; height: 56px;
  }
  .brand-square { width: 34px; height: 34px; background: var(--teal); }
  .brand-name { font-size: 26px; font-weight: 700; color: var(--gray-dark); }

  .slide-body { padding: 38px 48px 0 48px; }
  .data-panel { border: 2px solid var(--gray-light); }

  .data-table { width: 100%; border-collapse: collapse; font-size: 22px; }
  .data-table caption {
    caption-side: top; text-align: left;
    background: var(--teal); color: var(--paper);
    font-size: 30px; font-weight: 700; letter-spacing: 0.3px;
    padding: 12px 20px; height: 58px;
  }
  .data-table th, .data-table td {
    text-align: left; padding: 0 20px; height: 42px;
    border-bottom: 1px solid var(--gray-light);
  }
  .data-table thead th {
    font-weight: 700; color: var(--gray-dark); background: var(--paper);
    border-bottom: 2px solid var(--teal-light);
  }
  .data-table tbody td { font-weight: 700; color: var(--ink); }
  .data-table tbody tr:nth-child(even) td { background: var(--row-alt); }
  .col-major { width: 58%; }
  .col-grads { width: 18%; }
  .col-earn { width: 24%; }
</style>
</head>
<body>
<main class="deck">

  <section class="slide slide--one">
    <header class="slide-header slide-header--light">
      <h1 class="slide-title">TEXAS LABOR MARKET THEMES OF THE DAY</h1>
      <div class="brand"><span class="brand-square"></span><span class="brand-name">TLBavendish</span></div>
    </header>
    <div class="slide-body">
      <div class="data-panel">
        <table class="data-table">
          <caption>HIGHEST EARNING ASSOCIATE'S DEGREE PROGRAMS 2014</caption>
          <thead><tr><th class="col-major">Associate's Degree Graduate Major (TX) (50+)</th><th class="col-grads">Grads</th><th class="col-earn">Earnings</th></tr></thead>
          <tbody>
            <tr><td>Fire Protection</td><td>197</td><td>$68,582</td></tr>
            <tr><td>Physical Science Technologies/Chemical Process</td><td>676</td><td>$59,074</td></tr>
            <tr><td>Quality Control and Safety Technologies/Techs</td><td>146</td><td>$58,246</td></tr>
            <tr><td>Electrical and Power Transmission Installers</td><td>56</td><td>$58,149</td></tr>
            <tr><td>Fire Protection</td><td>197</td><td>$68,582</td></tr>
            <tr><td>Physical Science Technologies/Chemical Process</td><td>676</td><td>$59,074</td></tr>
            <tr><td>Quality Control and Safety Technologies/Techs</td><td>146</td><td>$58,246</td></tr>
            <tr><td>Electrical and Power Transmission Installers</td><td>56</td><td>$58,149</td></tr>
            <tr><td>Fire Protection</td><td>197</td><td>$68,582</td></tr>
            <tr><td>Physical Science Technologies/Chemical Process</td><td>676</td><td>$59,074</td></tr>
            <tr><td>Quality Control and Safety Technologies/Techs</td><td>146</td><td>$58,246</td></tr>
            <tr><td>Electrical and Power Transmission Installers</td><td>56</td><td>$58,149</td></tr>
            <tr><td>Fire Protection</td><td>197</td><td>$68,582</td></tr>
          </tbody>
        </table>
      </div>
    </div>
  </section>

  <section class="slide slide--two">
    <header class="slide-header slide-header--solid">
      <h1 class="slide-title">TEXAS LABOR MARKET THEMES OF THE DAY</h1>
      <div class="brand"><span class="brand-square"></span><span class="brand-name">TLBavendish</span></div>
    </header>
    <div class="slide-body">
      <div class="data-panel">
        <table class="data-table">
          <caption>HIGHEST EARNING ASSOCIATE'S DEGREE PROGRAMS 2014</caption>
          <thead><tr><th class="col-major">Associate's Degree Graduate Major (TX) (50+)</th><th class="col-grads">Grads</th><th class="col-earn">Earnings</th></tr></thead>
          <tbody>
            <tr><td>Fire Protection</td><td>197</td><td>$68,582</td></tr>
            <tr><td>Physical Science Technologies/Chemical Process</td><td>676</td><td>$59,074</td></tr>
            <tr><td>Quality Control and Safety Technologies/Techs</td><td>146</td><td>$58,246</td></tr>
            <tr><td>Electrical and Power Transmission Installers</td><td>56</td><td>$58,149</td></tr>
            <tr><td>Fire Protection</td><td>197</td><td>$68,582</td></tr>
            <tr><td>Physical Science Technologies/Chemical Process</td><td>676</td><td>$59,074</td></tr>
            <tr><td>Quality Control and Safety Technologies/Techs</td><td>146</td><td>$58,246</td></tr>
            <tr><td>Electrical and Power Transmission Installers</td><td>56</td><td>$58,149</td></tr>
            <tr><td>Fire Protection</td><td>197</td><td>$68,582</td></tr>
            <tr><td>Physical Science Technologies/Chemical Process</td><td>676</td><td>$59,074</td></tr>
            <tr><td>Quality Control and Safety Technologies/Techs</td><td>146</td><td>$58,246</td></tr>
            <tr><td>Electrical and Power Transmission Installers</td><td>56</td><td>$58,149</td></tr>
            <tr><td>Fire Protection</td><td>197</td><td>$68,582</td></tr>
          </tbody>
        </table>
      </div>
    </div>
  </section>

  <section class="slide slide--three">
    <header class="slide-header slide-header--pale">
      <h1 class="slide-title">TEXAS LABOR MARKET THEMES OF THE DAY</h1>
      <div class="brand"><span class="brand-square"></span><span class="brand-name">TLBavendish</span></div>
    </header>
    <div class="slide-body">
      <div class="data-panel">
        <table class="data-table">
          <caption>HIGHEST EARNING ASSOCIATE'S DEGREE PROGRAMS 2014</caption>
          <thead><tr><th class="col-major">Associate's Degree Graduate Major (TX) (50+)</th><th class="col-grads">Grads</th><th class="col-earn">Earnings</th></tr></thead>
          <tbody>
            <tr><td>Fire Protection</td><td>197</td><td>$68,582</td></tr>
            <tr><td>Physical Science Technologies/Chemical Process</td><td>676</td><td>$59,074</td></tr>
            <tr><td>Quality Control and Safety Technologies/Techs</td><td>146</td><td>$58,246</td></tr>
            <tr><td>Electrical and Power Transmission Installers</td><td>56</td><td>$58,149</td></tr>
            <tr><td>Fire Protection</td><td>197</td><td>$68,582</td></tr>
            <tr><td>Physical Science Technologies/Chemical Process</td><td>676</td><td>$59,074</td></tr>
            <tr><td>Quality Control and Safety Technologies/Techs</td><td>146</td><td>$58,246</td></tr>
            <tr><td>Electrical and Power Transmission Installers</td><td>56</td><td>$58,149</td></tr>
            <tr><td>Fire Protection</td><td>197</td><td>$68,582</td></tr>
            <tr><td>Physical Science Technologies/Chemical Process</td><td>676</td><td>$59,074</td></tr>
            <tr><td>Quality Control and Safety Technologies/Techs</td><td>146</td><td>$58,246</td></tr>
            <tr><td>Electrical and Power Transmission Installers</td><td>56</td><td>$58,149</td></tr>
            <tr><td>Fire Protection</td><td>197</td><td>$68,582</td></tr>
          </tbody>
        </table>
      </div>
    </div>
  </section>

</main>
</body>
</html>
```